North American Image Consultant needs a process design and a method design

I am an Image/style consultant who works with business professionals in the Toronto area. My product name is called " S.H.A.R.E." I help people understand how your " Style, Habits, Attitude, Reach and Energy. I help people create a professional appearance in a business casual/digital world, from head to toe. I work with them through all 4 seasons, to achieve consistency and confidence to help them look and feel amazing, inside and out.. easily and effortlessly. My main colour is aqua blue, I don't want any neon or primary colours. I would like it to appeal to both men and women ( but mostly women)
The final design should be an easy to follow path to success with an understanding of what S.H.A.R.E will do for them.

Target Market(s)

mid level executive business professionals 38-58 yrs old they want to look and feel amazing inside and out. They want to up their game, get the promotion, nail the interview , and feel they're relevant and taken seriously in a leadership way.

Font styles to use
Serif

Colors
b7a5cd
886aae
85cae6
33a6d7
33b8a4
f04a50
00a990
e34297
85acd3

Requirements
Must have
• A classy, casual feel. A positive feel good feeling
Nice to have
• A 3 colour balance ( Not black based)
Should not have
• Too many squares
too many squiggly lines.
Not too masculine/feminine
too childish/youthful
Not office focused or bank focused

```html
<!DOCTYPE html>
<html lang="en">
<head>
<meta charset="utf-8">
<title>S.H.A.R.E. Method</title>
<link href="https://fonts.googleapis.com/css2?family=Cinzel:wght@400&family=Roboto:wght@400;500&display=swap" rel="stylesheet">
<style>
  :root {
    --page-bg: #e8e8e8;
    --card-bg: #f4f4f4;
    --title-grey: #6b6b6b;
    --label-grey: #666666;
    --accent-teal: #7cc4c9;
    --pillar-teal: #7ec5cc;
    --pillar-blue: #86c8e6;
    --pale-letter: rgba(255, 255, 255, 0.6);
    --white: #ffffff;
  }
  * { margin: 0; padding: 0; box-sizing: border-box; }
  html, body {
    width: 1200px; height: 920px; overflow: hidden;
    background: var(--page-bg);
  }
  .method-card {
    position: absolute; left: 47px; top: 125px;
    width: 1106px; height: 670px;
    background: var(--card-bg);
  }
  .method-title {
    position: absolute; left: 0; right: 0; top: 20px;
    text-align: center;
    font-family: "Cinzel", serif; font-weight: 400;
    font-size: 150px; line-height: 1; letter-spacing: 2px;
    color: var(--title-grey);
  }
  .method-tagline {
    position: absolute; left: 0; right: 0; top: 166px;
    text-align: center;
    font-family: "Roboto", sans-serif; font-weight: 500;
    font-size: 25px; color: var(--accent-teal);
  }
  .pillar {
    position: absolute; top: 225px;
    width: 195px; height: 416px;
    border-radius: 42px;
    text-align: center;
  }
  .pillar--teal { background: var(--pillar-teal); }
  .pillar--blue { background: var(--pillar-blue); }
  .pillar-letter {
    position: absolute; left: 0; right: 0; top: 18px;
    font-family: "Cinzel", serif; font-size: 66px; line-height: 1;
    color: var(--pale-letter);
  }
  .pillar-name {
    position: absolute; left: 0; right: 0; top: 98px;
    font-family: "Cinzel", serif; font-size: 31px; line-height: 1;
    color: var(--label-grey);
  }
  .pillar-text {
    position: absolute; left: 18px; right: 18px; top: 153px;
    font-family: "Roboto", sans-serif; font-size: 21px; line-height: 1.3;
    color: var(--white);
  }
  .pillar-icon {
    position: absolute; left: 50%; top: 290px;
    width: 100px; height: 90px; margin-left: -50px;
  }
  .pillar-icon * { fill: none; stroke: var(--white); stroke-width: 3; stroke-linejoin: round; stroke-linecap: round; }
  .pillar-icon .solid { fill: var(--white); stroke: none; }
</style>
</head>
<body>
  <main class="method-card">
    <h1 class="method-title">S.H.A.R.E.</h1>
    <p class="method-tagline">Creating individual style with direction and purpose</p>

    <section class="pillar pillar--teal" style="left:35px">
      <div class="pillar-letter">S</div>
      <h2 class="pillar-name">Style</h2>
      <p class="pillar-text">Assert your level of authority</p>
      <svg class="pillar-icon" viewBox="0 0 100 90" aria-hidden="true">
        <path d="M18 62 L10 30 L32 46 L50 18 L68 46 L90 30 L82 62 Z"/>
        <path d="M18 72 H82"/>
        <circle cx="10" cy="26" r="4"/><circle cx="50" cy="14" r="4"/><circle cx="90" cy="26" r="4"/>
        <path d="M50 40 L56 50 L50 60 L44 50 Z"/>
      </svg>
    </section>

    <section class="pillar pillar--blue" style="left:241px">
      <div class="pillar-letter">H</div>
      <h2 class="pillar-name">Habits</h2>
      <p class="pillar-text">Shape your daily image</p>
      <svg class="pillar-icon" viewBox="0 0 100 90" aria-hidden="true">
        <path d="M20 60 A32 32 0 0 1 50 13"/>
        <path d="M80 30 A32 32 0 0 1 50 77"/>
        <circle cx="50" cy="45" r="22"/>
        <circle cx="50" cy="33" r="5"/>
        <path d="M43 62 V44 H57 V62"/>
        <circle cx="14" cy="22" r="3"/><path d="M11 40 V28 H17 V40"/>
        <circle cx="86" cy="62" r="3"/><path d="M83 80 V68 H89 V80"/>
      </svg>
    </section>

    <section class="pillar pillar--teal" style="left:453px">
      <div class="pillar-letter">A</div>
      <h2 class="pillar-name">Attitude</h2>
      <p class="pillar-text">Your energy field</p>
      <svg class="pillar-icon" viewBox="0 0 100 90" aria-hidden="true">
        <path d="M28 20 A34 34 0 0 0 28 70"/>
        <path d="M72 20 A34 34 0 0 1 72 70"/>
        <path d="M18 10 A46 46 0 0 0 18 80"/>
        <path d="M82 10 A46 46 0 0 1 82 80"/>
        <circle class="solid" cx="50" cy="36" r="9"/>
        <path class="solid" d="M34 62 A16 14 0 0 1 66 62 Z"/>
      </svg>
    </section>

    <section class="pillar pillar--blue" style="left:664px">
      <div class="pillar-letter">R</div>
      <h2 class="pillar-name">Reach</h2>
      <p class="pillar-text">Empowerment</p>
      <svg class="pillar-icon" viewBox="0 0 100 90" aria-hidden="true">
        <circle cx="50" cy="32" r="28"/>
        <circle cx="50" cy="32" r="19"/>
        <path d="M50 21 L53 29 L61 29 L55 34 L57 42 L50 37 L43 42 L45 34 L39 29 L47 29 Z"/>
        <path d="M34 55 L24 84 L32 78 L38 86 L44 62"/>
        <path d="M66 55 L76 84 L68 78 L62 86 L56 62"/>
      </svg>
    </section>

    <section class="pillar pillar--teal" style="left:875px">
      <div class="pillar-letter">E</div>
      <h2 class="pillar-name">Energy</h2>
      <p class="pillar-text">Gain More. Spend less</p>
      <svg class="pillar-icon" viewBox="0 0 100 90" aria-hidden="true">
        <circle cx="50" cy="47" r="40" stroke-width="4"/>
        <path d="M46 24 V50 L58 62" stroke-width="4"/>
      </svg>
    </section>
  </main>
</body>
</html>
```